Local Roofing/Construction company business needs new biz card design

We need a new business card design, current cards are from the start of this operation and generic at best. We are a local Construction Company (General Contractor) with a majority of our work originating from insurance claims-exterior finish work is the main focus (Roofs-Siding-Gutters etc). Heavily involved with homeowners and the low ball offers they receive from insurance company's after a insurable event takes place. I have attached some of our original logo file(s) below.

```html
<!DOCTYPE html>
<html lang="de">
<head>
<meta charset="utf-8">
<title>Brightway Construction – Visitenkarte</title>
<link href="https://fonts.googleapis.com/css2?family=Roboto+Condensed:ital,wght@0,400;0,700;1,700&display=swap" rel="stylesheet">
<style>
  :root {
    --brand-green: #55bc6f;
    --ink-dark: #0f1f1f;
    --paper: #f9f7f4;
    --white: #ffffff;
    --stage: #eceeee;
  }
  * { margin: 0; padding: 0; box-sizing: border-box; }
  html, body {
    width: 1199px; height: 1200px; overflow: hidden;
    background: var(--stage);
    font-family: "Roboto Condensed", "Arial Narrow", sans-serif;
  }
  .card {
    position: absolute; left: 169px; width: 860px; height: 504px;
  }
  .card--front { top: 77px; background: var(--brand-green); color: var(--white); }
  .card--back { top: 618px; background: var(--paper); }

  .wordmark {
    position: absolute; display: flex; align-items: center; gap: 18px;
    font-weight: 700; text-transform: uppercase; line-height: 1;
  }
  .wordmark__square { display: block; flex: none; }
  .wordmark__text { display: flex; flex-direction: column; gap: 6px; }

  .card--front .wordmark {
    left: 50%; top: 142px; transform: translate(-50%, -50%);
    color: var(--ink-dark);
  }
  .card--front .wordmark__square { width: 92px; height: 92px; background: var(--ink-dark); }
  .card--front .wordmark__name { font-size: 62px; letter-spacing: 1px; }
  .card--front .wordmark__line { font-size: 37px; letter-spacing: 3px; }

  .holder { position: absolute; left: 78px; top: 330px; }
  .holder__name { font-size: 36px; font-weight: 700; font-style: italic; letter-spacing: 0.3px; }
  .holder__role { margin-top: 10px; font-size: 20px; font-weight: 400; }

  .contact-list { position: absolute; right: 36px; top: 284px; list-style: none; }
  .contact-list__item {
    display: flex; align-items: center; justify-content: flex-end;
    gap: 17px; height: 37px; font-size: 20px; font-weight: 400;
  }
  .contact-list__item--address { margin-top: 16px; }
  .contact-icon { width: 26px; height: 26px; flex: none; }

  .card--back .wordmark {
    left: 50%; top: 50%; transform: translate(-50%, -50%);
    flex-direction: column; gap: 22px; color: var(--brand-green); text-align: center;
  }
  .card--back .wordmark__square { width: 160px; height: 160px; background: var(--brand-green); }
  .card--back .wordmark__text { align-items: center; }
  .card--back .wordmark__name { font-size: 50px; letter-spacing: 1px; }
  .card--back .wordmark__line { font-size: 30px; letter-spacing: 3px; }
</style>
</head>
<body>

<section class="card card--front" aria-label="Vorderseite">
  <div class="wordmark">
    <span class="wordmark__square"></span>
    <span class="wordmark__text">
      <span class="wordmark__name">Brightway</span>
      <span class="wordmark__line">Construction</span>
    </span>
  </div>

  <div class="holder">
    <p class="holder__name">Lukas Brenner</p>
    <p class="holder__role">Geschäftsführer</p>
  </div>

  <ul class="contact-list">
    <li class="contact-list__item">+49 1500 000000
      <svg class="contact-icon" viewBox="0 0 26 26" aria-hidden="true">
        <rect width="26" height="26" rx="4" fill="#fff"/>
        <path d="M9 6.5c.8 0 1.5 2.4 1.5 3s-1.2 1-1.2 1.6c.4 2 2.3 3.9 4.3 4.4.6 0 1-1.2 1.6-1.2s3 .7 3 1.5-1 2.7-2.5 2.7C11 18.5 7.5 15 7.5 10.3 7.5 8 8.2 6.5 9 6.5z" fill="#0f1f1f"/>
      </svg>
    </li>
    <li class="contact-list__item">lukas@brightwaybau.com
      <svg class="contact-icon" viewBox="0 0 26 26" aria-hidden="true">
        <rect width="26" height="26" rx="4" fill="#fff"/>
        <rect x="6" y="8" width="14" height="10" rx="1" fill="#0f1f1f"/>
        <path d="M6.5 8.5 13 13.5l6.5-5" stroke="#fff" stroke-width="1.3" fill="none"/>
      </svg>
    </li>
    <li class="contact-list__item">www.brightwaybau.com
      <svg class="contact-icon" viewBox="0 0 26 26" aria-hidden="true">
        <rect width="26" height="26" rx="4" fill="#fff"/>
        <circle cx="13" cy="13" r="7" fill="#0f1f1f"/>
        <path d="M6 13h14M13 6c-3 3.5-3 10.5 0 14M13 6c3 3.5 3 10.5 0 14" stroke="#fff" stroke-width="1.1" fill="none"/>
      </svg>
    </li>
    <li class="contact-list__item contact-list__item--address">Musterweg 12, Beispielstadt
      <svg class="contact-icon" viewBox="0 0 26 26" aria-hidden="true">
        <rect width="26" height="26" rx="4" fill="#fff"/>
        <path d="M13 5.5a5 5 0 0 1 5 5c0 3.6-5 8.5-5 8.5s-5-4.9-5-8.5a5 5 0 0 1 5-5z" fill="#0f1f1f"/>
        <circle cx="13" cy="10.5" r="1.8" fill="#fff"/>
        <rect x="8" y="19.5" width="10" height="1.5" fill="#0f1f1f"/>
      </svg>
    </li>
  </ul>
</section>

<section class="card card--back" aria-label="Rückseite">
  <div class="wordmark">
    <span class="wordmark__square"></span>
    <span class="wordmark__text">
      <span class="wordmark__name">Brightway</span>
      <span class="wordmark__line">Construction</span>
    </span>
  </div>
</section>

</body>
</html>
```